Brindlow Website + Logo

I'm creating a quillbox style site and I will be using your submission to pitch the concept to investors.

I've attached my initial attempt which you are welcome to continue building on, or you can build it again yourself.

- The buttons "What's happening", "Following" and "Events" are important to the current design for functionality, but you can change the "look and feel".
- Mock-up advertising would be helpful for the pitch. Please feel free to imagine how this would be implemented into the website. I currently have space integrated into the feed + right side but you can change this.
- The old logo is currently at the top of the screen. Please feel free to reimagine this, as I am paying for a logo as well.

Happy to answer any other questions.

Thanks,

Ivan.

```html
<!DOCTYPE html>
<html lang="en">
<head>
<meta charset="utf-8">
<title>Brindlow – customize feed</title>
<link rel="stylesheet" href="https://fonts.googleapis.com/css2?family=Playfair+Display:wght@400;500;600&display=swap">
<style>
  :root {
    --chrome: #929292;
    --chrome-dark: #858585;
    --tab: #9c9c9c;
    --brand: #0a7a2a;
    --active: #004400;
    --panel: #ffffff;
    --ink: #333333;
    --black: #111111;
    --border: #d4d4d4;
    --close: #ff0000;
    --ad-a: #e4efe6;
    --ad-b: #c9dccd;
    --ad-label: #8a8a8a;
  }
  * { box-sizing: border-box; margin: 0; padding: 0; }
  html, body { width: 1200px; height: 2243px; overflow: hidden; }
  body {
    position: relative;
    background: var(--chrome);
    font-family: "Playfair Display", Georgia, serif;
    color: var(--ink);
  }

  /* Header */
  .site-header { position: absolute; left: 0; top: 0; width: 1200px; height: 265px; background: var(--chrome); }
  .brand-lockup { position: absolute; left: 22px; top: 22px; display: flex; align-items: center; gap: 14px; }
  .brand-dot { width: 66px; height: 66px; border-radius: 50%; background: var(--brand); }
  .brand-name { font-size: 30px; font-weight: 500; color: var(--brand); }
  .site-title { position: absolute; left: 0; width: 1200px; top: 24px; text-align: center; font-size: 44px; font-weight: 500; color: var(--brand); letter-spacing: 1px; }
  .header-tools { position: absolute; top: 40px; right: 40px; display: flex; gap: 24px; align-items: center; }
  .header-tools svg { height: 32px; stroke: #333; fill: none; stroke-width: 2.4; }

  .feed-tabs { position: absolute; top: 176px; left: 0; width: 1200px; height: 89px; }
  .feed-tab {
    position: absolute; top: 0; width: 162px; height: 89px;
    background: var(--tab); border-radius: 14px 14px 0 0;
    box-shadow: 0 -2px 6px rgba(0,0,0,.14);
    font-size: 17px; line-height: 23px; color: #222;
    display: flex; align-items: flex-end; padding: 0 0 12px 38px;
  }
  .feed-tab.is-active { background: var(--active); color: #d8e6d8; }
  .tab-happening { left: 159px; }
  .tab-following { left: 404px; justify-content: center; padding-left: 0; padding-bottom: 20px; }
  .tab-customize { left: 646px; }
  .tab-events { left: 870px; justify-content: center; padding-left: 0; padding-bottom: 18px; }

  /* Panel */
  .customize-panel { position: absolute; left: 0; top: 265px; width: 1200px; height: 1538px; background: var(--panel); }
  .panel-heading { position: absolute; left: 59px; top: 36px; font-size: 50px; font-weight: 600; color: var(--black); letter-spacing: 2.4px; white-space: nowrap; }
  .close-button {
    position: absolute; left: 966px; top: 29px; width: 208px; height: 64px;
    background: var(--close); color: #fff; font-size: 35px; border-radius: 6px;
    display: flex; align-items: center; justify-content: center;
  }
  .topic {
    position: absolute; width: 383px; height: 98px;
    border: 1px solid var(--border); border-radius: 10px; background: #fff;
    box-shadow: 0 2px 6px rgba(0,0,0,.05);
    display: flex; align-items: center; justify-content: center;
    font-size: 33px; color: var(--ink); letter-spacing: 1px;
  }
  .topic.is-selected { background: var(--ink); color: #fff; border-color: var(--ink); }
  .col-left { left: 62px; }
  .col-right { left: 755px; }

  /* Advertising */
  .ad-slot { position: absolute; }
  .ad-label { font-size: 13px; letter-spacing: 2px; text-transform: uppercase; color: var(--ad-label); margin-bottom: 6px; text-align: center; }
  .ad-creative {
    border-radius: 10px; border: 1px dashed #9fbfa6;
    background: linear-gradient(160deg, var(--ad-a), var(--ad-b));
    display: flex; align-items: center; justify-content: center; text-align: center;
    font-size: 18px; color: #4c6b53; line-height: 26px;
  }
  .ad-skyscraper { left: 520px; top: 191px; width: 160px; }
  .ad-skyscraper .ad-creative { height: 600px; }
  .ad-banner { left: 236px; top: 1410px; width: 728px; }
  .ad-banner .ad-creative { height: 90px; }

  /* Footer */
  .site-footer { position: absolute; left: 0; top: 1803px; width: 1200px; height: 440px; background: var(--chrome); }
  .footer-brand { position: absolute; left: 59px; top: 150px; display: flex; align-items: center; gap: 18px; }
  .footer-brand .brand-dot { width: 120px; height: 120px; }
  .footer-brand .brand-name { font-size: 34px; }
  .footer-links { position: absolute; list-style: none; font-size: 18px; line-height: 27px; color: #1c1c1c; }
  .links-feed { left: 399px; top: 164px; font-size: 19px; }
  .links-account { left: 620px; top: 160px; }
  .links-legal { left: 851px; top: 153px; line-height: 23.5px; }
</style>
</head>
<body>
  <header class="site-header">
    <div class="brand-lockup"><div class="brand-dot"></div><span class="brand-name">Brindlow</span></div>
    <div class="site-title">Brindlow</div>
    <div class="header-tools">
      <svg viewBox="0 0 32 32" width="32" aria-label="search"><circle cx="14" cy="14" r="9"/><line x1="21" y1="21" x2="28" y2="28"/></svg>
      <svg viewBox="0 0 40 32" width="40" aria-label="menu"><line x1="2" y1="10" x2="38" y2="10"/><line x1="2" y1="16" x2="38" y2="16"/><line x1="2" y1="22" x2="38" y2="22"/></svg>
      <svg viewBox="0 0 32 32" width="32" aria-label="account"><circle cx="16" cy="10" r="7"/><path d="M4 30 v-4 a8 8 0 0 1 8-8 h8 a8 8 0 0 1 8 8 v4 z"/></svg>
    </div>
    <nav class="feed-tabs">
      <div class="feed-tab tab-happening">what’s<br>happening</div>
      <div class="feed-tab tab-following">following</div>
      <div class="feed-tab tab-customize is-active">customize<br>feed</div>
      <div class="feed-tab tab-events">events</div>
    </nav>
  </header>

  <main class="customize-panel">
    <h1 class="panel-heading">customize what you want to see</h1>
    <div class="close-button">Close</div>

    <div class="topic col-left" style="top:194px">Politics</div>
    <div class="topic col-left" style="top:326px">News</div>
    <div class="topic col-left" style="top:453px">Gaming</div>
    <div class="topic col-left" style="top:578px">Shopping</div>
    <div class="topic col-left" style="top:719px">Movies</div>
    <div class="topic col-left" style="top:861px">Travel</div>
    <div class="topic col-left" style="top:1004px">Crypto</div>
    <div class="topic col-left" style="top:1148px">World</div>
    <div class="topic col-left" style="top:1288px">People</div>

    <div class="topic col-right is-selected" style="top:191px">Tech</div>
    <div class="topic col-right" style="top:326px">Science</div>
    <div class="topic col-right" style="top:459px">Near you</div>
    <div class="topic col-right" style="top:586px">TV</div>
    <div class="topic col-right" style="top:727px">Sport</div>
    <div class="topic col-right" style="top:870px">Memes</div>
    <div class="topic col-right" style="top:1016px">Food</div>
    <div class="topic col-right" style="top:1148px">Health</div>

    <aside class="ad-slot ad-skyscraper">
      <div class="ad-label">Sponsored</div>
      <div class="ad-creative" role="img" aria-label="advertiser creative, tall side placement">Your ad<br>here<br>160 × 600</div>
    </aside>
    <aside class="ad-slot ad-banner">
      <div class="ad-label">Sponsored</div>
      <div class="ad-creative" role="img" aria-label="advertiser creative, banner placement">Your ad here · 728 × 90</div>
    </aside>
  </main>

  <footer class="site-footer">
    <div class="footer-brand"><div class="brand-dot"></div><span class="brand-name">Brindlow</span></div>
    <ul class="footer-links links-feed">
      <li>what’s happening</li><li>folowing</li><li>customize feed</li><li>events</li>
    </ul>
    <ul class="footer-links links-account">
      <li>sign up</li><li>sign in</li><li>forgot password</li>
    </ul>
    <ul class="footer-links links-legal">
      <li>report an issue</li><li>feedback</li><li>privacy policy</li><li>terms and condition</li>
    </ul>
  </footer>
</body>
</html>
```